National Chemical Line for Homeowners Needs a Logo & Label Design.

We need a logo and label design for a New National Chemical Company that is Private Labeling/Creating Cleaning Chemicals for Homeowners to use themselves. These chemicals will be used to clean carpets, hard surfaces, remove cat & dog stains and odors and many other products to come.
The first product will be for homeowners to remove cat & dog stains and odors from their carpets. We would like the label for the front and back of a 32 oz. white spray bottle. Go to www.brellowsupply.example and reference Part# 41KPL7.
We want the bottle/label to stand out on the grocery store shelves. We want it to be simple to read, eye catching, have a simple name and explain what the product does . The back of the bottle will have directions, caution statements, etc.
The Name of our Company is Vanta Meridian. It does have a trademark. We want the word "Vanta" to stand out and the word "meridian to only be present, that way the word Vanta will gain traction with the customer.
We want the color scheme to be Pinks & Blues.

```html
<!DOCTYPE html>
<html lang="en">
<head>
<meta charset="utf-8">
<title>Vanta Meridian – Cat &amp; Dog Stains &amp; Odors Remover Label</title>
<link href="https://fonts.googleapis.com/css2?family=Montserrat:ital,wght@0,600;0,800;0,900;1,900&family=Poppins:wght@500&display=swap" rel="stylesheet">
<style>
  :root {
    --page-bg: #eef2fd;
    --royal-blue: #1a3fc4;
    --deep-blue: #142fa8;
    --hot-pink: #ea3d99;
    --soft-pink: #f59ccb;
    --blush: #fde7f2;
    --white: #ffffff;
    --silver: #c9cdd8;
    --badge-blue: #bfe0fb;
  }
  html, body {
    margin: 0;
    padding: 0;
    width: 1200px;
    height: 1087px;
    overflow: hidden;
    background: var(--page-bg);
  }
  .label {
    position: absolute;
    left: 192px;
    top: 42px;
    width: 815px;
    height: 1002px;
    display: block;
  }
  .brand-name { font-family: "Montserrat", sans-serif; font-weight: 800; fill: var(--royal-blue); }
  .tag-text { font-family: "Montserrat", sans-serif; font-weight: 900; fill: var(--white); }
  .headline { font-family: "Montserrat", sans-serif; font-weight: 900; fill: var(--royal-blue); }
  .badge-text { font-family: "Montserrat", sans-serif; font-weight: 900; font-style: italic; fill: var(--royal-blue); }
  .feature-label { font-family: "Poppins", sans-serif; font-weight: 500; fill: var(--white); font-size: 14px; }
  .volume { font-family: "Montserrat", sans-serif; font-weight: 600; fill: var(--white); }
  .feature-icon { fill: none; stroke: var(--white); stroke-width: 2; stroke-linecap: round; stroke-linejoin: round; }
</style>
</head>
<body>
<svg class="label" viewBox="0 0 830 1020" xmlns="http://www.w3.org/2000/svg" aria-label="Vanta Meridian cat and dog stains and odors remover front label">
  <defs>
    <clipPath id="label-shape">
      <path d="M10,130 Q400,-40 800,40 Q830,50 828,95 L828,950 Q828,1016 770,1018 L70,1018 Q12,1016 12,960 Z"/>
    </clipPath>
    <radialGradient id="pink-glow" cx="0.42" cy="0.62" r="0.75">
      <stop offset="0" stop-color="#ffffff"/>
      <stop offset="0.35" stop-color="var(--blush)"/>
      <stop offset="0.75" stop-color="var(--soft-pink)"/>
      <stop offset="1" stop-color="#ee6fb4"/>
    </radialGradient>
    <linearGradient id="pets-tone" x1="0" y1="0" x2="1" y2="1">
      <stop offset="0" stop-color="#8a7a66"/>
      <stop offset="0.6" stop-color="#3b2a1f"/>
      <stop offset="1" stop-color="#1c1512"/>
    </linearGradient>
  </defs>

  <g clip-path="url(#label-shape)">
    <rect class="label-backdrop" width="830" height="1020" fill="url(#pink-glow)"/>

    <!-- brand -->
    <g class="brand">
      <text class="brand-name" x="560" y="165" font-size="112" text-anchor="middle">Vanta</text>
      <text class="brand-name" x="560" y="210" font-size="32" text-anchor="middle" letter-spacing="2">MERIDIAN</text>
    </g>

    <!-- headline -->
    <g class="headline-block" transform="rotate(-7 70 500)">
      <rect class="tag" x="70" y="246" width="258" height="60" fill="var(--hot-pink)"/>
      <text class="tag-text" x="199" y="291" font-size="38" text-anchor="middle">CAT &amp; DOG</text>
      <text class="headline" x="66" y="398" font-size="100" textLength="700" lengthAdjust="spacingAndGlyphs">STAINS &amp; ODORS</text>
      <text class="headline" x="66" y="492" font-size="100" textLength="385" lengthAdjust="spacingAndGlyphs">REMOVER</text>
      <rect class="tag" x="462" y="418" width="322" height="70" fill="var(--hot-pink)"/>
      <text class="tag-text" x="623" y="468" font-size="46" text-anchor="middle" textLength="296" lengthAdjust="spacingAndGlyphs">FOR CARPET</text>
    </g>

    <!-- bottom band -->
    <path class="wave-silver" d="M0,735 C200,680 350,770 500,712 S760,602 830,620 L830,660 C760,645 620,700 500,750 S200,730 0,775 Z" fill="var(--silver)"/>
    <path class="wave-blue" d="M0,770 C200,722 350,800 500,745 S760,640 830,655 L830,1020 L0,1020 Z" fill="var(--royal-blue)"/>
    <path class="wave-line" d="M0,752 C200,702 350,788 500,730 S760,622 830,638" fill="none" stroke="var(--white)" stroke-width="8"/>

    <!-- pets photo -->
    <rect class="pets-photo" x="450" y="470" width="305" height="350" rx="40" fill="url(#pets-tone)" role="img" aria-label="Photo of a tabby cat sitting beside a tricolour dog"/>

    <!-- badge -->
    <g class="power-badge">
      <circle cx="220" cy="640" r="105" fill="var(--badge-blue)" opacity="0.85"/>
      <g transform="rotate(-12 220 640)">
        <text class="badge-text" x="220" y="608" font-size="34" text-anchor="middle">SUPERIOR</text>
        <text class="badge-text" x="220" y="642" font-size="32" text-anchor="middle">CLEANING</text>
        <text class="badge-text" x="220" y="684" font-size="44" text-anchor="middle">POWER</text>
      </g>
    </g>

    <!-- features -->
    <g class="features">
      <g class="feature">
        <circle class="feature-icon" cx="148" cy="895" r="37"/>
        <path class="feature-icon" d="M126,915 L134,893 L170,893 L162,915 Z"/>
        <path class="feature-icon" d="M150,872 l2,6 6,2 -6,2 -2,6 -2,-6 -6,-2 6,-2 Z M166,866 l1,3 3,1 -3,1 -1,3 -1,-3 -3,-1 3,-1 Z"/>
        <text class="feature-label" x="148" y="950" text-anchor="middle">ALL</text>
        <text class="feature-label" x="148" y="966" text-anchor="middle">CARPETS</text>
      </g>
      <g class="feature">
        <circle class="feature-icon" cx="272" cy="895" r="37"/>
        <circle class="feature-icon" cx="260" cy="884" r="8"/>
        <circle class="feature-icon" cx="284" cy="884" r="8"/>
        <circle class="feature-icon" cx="272" cy="907" r="8"/>
        <text class="feature-label" x="272" y="950" text-anchor="middle">FRESH</text>
        <text class="feature-label" x="272" y="966" text-anchor="middle">FREGRANCE</text>
      </g>
      <g class="feature">
        <circle class="feature-icon" cx="412" cy="895" r="37"/>
        <path class="feature-icon" d="M396,888 A18,18 0 0 1 424,878 M428,900 A18,18 0 0 1 404,914 M418,874 l7,4 -3,7 M408,918 l-6,-4 3,-7"/>
        <text class="feature-label" x="412" y="950" text-anchor="middle">PREVENT</text>
        <text class="feature-label" x="412" y="966" text-anchor="middle">REPEAT MARKING</text>
      </g>
      <g class="feature">
        <circle class="feature-icon" cx="532" cy="895" r="37"/>
        <ellipse class="feature-icon" cx="532" cy="905" rx="11" ry="9"/>
        <circle class="feature-icon" cx="517" cy="888" r="4"/>
        <circle class="feature-icon" cx="527" cy="879" r="4"/>
        <circle class="feature-icon" cx="537" cy="879" r="4"/>
        <circle class="feature-icon" cx="547" cy="888" r="4"/>
        <text class="feature-label" x="532" y="950" text-anchor="middle">FOR</text>
        <text class="feature-label" x="532" y="966" text-anchor="middle">ALL PETS</text>
      </g>
      <text class="volume" x="730" y="935" font-size="42" text-anchor="middle">1L.</text>
    </g>
  </g>
</svg>
</body>
</html>
```